Hadley & Partners, LLC Business Card 2016

We need a new business card design for a very important trade show coming up.

We are a compliance Consulting Firm. Our clients are stock brokerage firms and investment advisers.

I would like our logo on both sides of the card.

Info in the front of the card shold include:

Logo
First & Last Name
Title
Office #
Cell #
Email
Company Address (42 W. Calloway St., Suite 300 Pasadena, CA 91417

Back of the card should include the logo and url: www.hadleypartnersgroup.com

Target Market(s)

Stock Brokerage Firms and Investment Advisers

Industry/Entity Type

Financial Service

Contact Information for Business Card

Marcus J. Pellew
President
42 W. Calloway St., Suite 300
Pasadena, CA 91417
O 626.555.0147 ext. 204
C 818.555.0193
Email: marcus@hadleypartnersgroup.com
www.hadleypartnersgroup.com

Requirements
Nice to have
• The back of the card could be black with the logo with the white letters.
• I do want the front of the card to at least have the color logo with the black "Hadley & Partners Lettering.

```html
<!DOCTYPE html>
<html lang="en">
<head>
<meta charset="utf-8">
<title>Hadley &amp; Partners — Business Card</title>
<link href="https://fonts.googleapis.com/css2?family=Archivo:wght@700;800&family=Arimo:wght@400&family=Titillium+Web:wght@400&display=swap" rel="stylesheet">
<style>
  :root {
    --board-light: #e6e6e6;
    --board-dark: #4e4e4e;
    --card-white: #ffffff;
    --card-charcoal: #3a3a3b;
    --ink-dark: #3b3b3d;
    --brand-red: #b51c1c;
    --deco-faint: #ececec;
    --spot-black: #000000;
    --label-ink: #2e2e2e;
    --text-white: #ffffff;
  }
  * { margin: 0; padding: 0; box-sizing: border-box; }
  html, body { width: 1200px; height: 960px; overflow: hidden; }
  body {
    position: relative;
    background: radial-gradient(ellipse 700px 620px at 300px 470px, var(--board-light) 0%, #b4b4b4 45%, var(--board-dark) 100%);
    font-family: "Arimo", Arial, sans-serif;
  }
  .card {
    position: absolute;
    left: 341px;
    width: 518px;
    height: 298px;
    overflow: hidden;
    box-shadow: 4px 5px 6px rgba(0,0,0,0.45);
  }
  .card--front { top: 20px; background: var(--card-white); }
  .card--spot-uv { top: 331px; background: var(--card-white); }
  .card--back { top: 642px; background: var(--card-charcoal); }

  .corner-block {
    position: absolute; left: 0; top: 0; width: 205px; height: 205px;
  }
  .card--front .corner-block { background: var(--deco-faint); }
  .card--spot-uv .corner-block { background: var(--spot-black); }

  .name-bar {
    position: absolute; left: 0; top: 234px; width: 21px; height: 35px;
    background: linear-gradient(90deg, #8e1010, var(--brand-red));
  }
  .person-name {
    position: absolute; left: 34px; top: 231px;
    font-family: "Archivo", Arial, sans-serif; font-weight: 800;
    font-size: 21px; line-height: 24px; color: var(--ink-dark); letter-spacing: 0.3px;
    white-space: nowrap;
  }
  .person-title {
    position: absolute; left: 34px; top: 258px;
    font-family: "Archivo", Arial, sans-serif; font-weight: 700;
    font-size: 12px; line-height: 14px; color: var(--brand-red); letter-spacing: 1.6px;
  }

  .brand-lockup {
    position: absolute; display: flex; flex-direction: column; align-items: center; gap: 8px;
    font-family: "Archivo", Arial, sans-serif; font-weight: 800;
  }
  .brand-lockup .brand-mark { width: 30px; height: 30px; background: var(--brand-red); flex: none; }
  .card--front .brand-lockup { left: 318px; top: 186px; width: 180px; }
  .card--front .brand-name { font-size: 16px; line-height: 20px; color: var(--ink-dark); white-space: nowrap; }
  .card--back .brand-lockup { left: 0; right: 0; top: 44px; flex-direction: row; justify-content: center; gap: 14px; }
  .card--back .brand-name { font-size: 22px; line-height: 30px; color: var(--text-white); white-space: nowrap; }

  .contact-list { position: absolute; left: 124px; top: 124px; list-style: none; }
  .contact-row { display: flex; align-items: center; height: 47px; }
  .contact-icon { width: 34px; height: 34px; flex: none; margin-right: 8px; }
  .contact-text { font-size: 14px; line-height: 17.5px; color: var(--text-white); white-space: nowrap; }

  .view-label {
    position: absolute; left: 896px;
    font-family: "Titillium Web", Arial, sans-serif; font-size: 42px; line-height: 55px;
    color: var(--label-ink);
  }
  .view-label--front { top: 145px; }
  .view-label--spot { top: 430px; }
  .view-label--back { top: 754px; }
</style>
</head>
<body>
  <section class="card card--front" aria-label="Card front">
    <div class="corner-block" aria-hidden="true"></div>
    <div class="name-bar"></div>
    <div class="person-name">MARCUS J. PELLEW</div>
    <div class="person-title">PRESIDENT</div>
    <div class="brand-lockup">
      <span class="brand-mark"></span>
      <span class="brand-name">HADLEY &amp; PARTNERS</span>
    </div>
  </section>

  <section class="card card--spot-uv" aria-label="Card front spot UV layer">
    <div class="corner-block" role="img" aria-label="Spot UV gloss area over the front decoration"></div>
  </section>

  <section class="card card--back" aria-label="Card back">
    <div class="brand-lockup">
      <span class="brand-mark"></span>
      <span class="brand-name">HADLEY &amp; PARTNERS</span>
    </div>
    <ul class="contact-list">
      <li class="contact-row">
        <svg class="contact-icon" viewBox="0 0 34 34" aria-hidden="true">
          <circle cx="17" cy="17" r="15.5" fill="none" stroke="#fff" stroke-width="2"/>
          <path d="M12.5 10.5 l3 -1 l1.8 4.2 l-2 1.3 q1 3 3.6 5 l1.6 -1.8 l4 2 l-0.8 3 q-3.5 1.5 -8 -3.5 q-4.6 -5.2 -3.2 -9.2z" fill="none" stroke="#fff" stroke-width="1.6" stroke-linejoin="round"/>
        </svg>
        <span class="contact-text">(626) 555-0147 ext. 204<br>(818) 555-0193 (Cell)</span>
      </li>
      <li class="contact-row">
        <svg class="contact-icon" viewBox="0 0 34 34" aria-hidden="true">
          <circle cx="17" cy="17" r="15.5" fill="none" stroke="#fff" stroke-width="2"/>
          <g fill="none" stroke="#fff" stroke-width="1.3">
            <circle cx="17" cy="17" r="8"/>
            <ellipse cx="17" cy="17" rx="3.6" ry="8"/>
            <line x1="9" y1="17" x2="25" y2="17"/>
            <line x1="17" y1="9" x2="17" y2="25"/>
            <path d="M10.5 12.5 h13 M10.5 21.5 h13"/>
          </g>
        </svg>
        <span class="contact-text">marcus@hadleypartnersgroup.com<br>www.hadleypartnersgroup.com</span>
      </li>
      <li class="contact-row">
        <svg class="contact-icon" viewBox="0 0 34 34" aria-hidden="true">
          <circle cx="17" cy="17" r="15.5" fill="none" stroke="#fff" stroke-width="2"/>
          <path d="M17 26 q-6.5 -7.5 -6.5 -11.5 a6.5 6.5 0 0 1 13 0 q0 4 -6.5 11.5z" fill="#fff"/>
          <circle cx="17" cy="14.5" r="2.6" fill="var(--card-charcoal)"/>
        </svg>
        <span class="contact-text">42 W. Calloway St., Suite 300<br>Pasadena, CA 91417</span>
      </li>
    </ul>
  </section>

  <div class="view-label view-label--front">Front</div>
  <div class="view-label view-label--spot">Front<br>Spot UV</div>
  <div class="view-label view-label--back">Back</div>
</body>
</html>
```